Web Design Project

i'm looking for a sleek modern design i can use for a web site that deals with.
Intelligent Data Capture
Accounts Payable Solutions for faster processing based on our scanning solution.
ultimately we are a intelligent scanning software.

here is a great website, that does exactly what we do, and we like to have most of their services and products.

so something in this idea would be great.
www.varnol.com

so i guess i want a good landing/home page which is smartly designed so users will be inclined to leave their information.

and then information pages.

also i dont need any cms for you to include, i only need you to hook the html hooks for RANK Kettle as i already have a CMS and need it to hook in to that, i am including links to that cheat sheet.
so it is easier when included as you create the Theme.

http://www.rankkettle.com/how-to-create-website-template.html
http://www.rankkettle.com/cheat-sheet.html
Updates

Hi Guys sorry for the long pause in design, but here is where we stand.

what ever design i choose, i need that designer to customize a few things for me based on design that was designed.
and i will need designer to match that them to work with RANK Kettle
here is the cheat sheet for the hooks that we need to match and make it work.
if you have any questions let me know.

otherwise i look forward to working with you. and good luck.

Target Market(s)

CFO's AP Managers, mostly ppl who are not Tech freindly

Industry/Entity Type

Software

Requirements
Must have
• i need on home page, the rotating banner should have 1 ability to place clipvane links to show videos, and also ability to add buttons on these rotating banners that will allow forms to pop up take to another page.

```html
<!DOCTYPE html>
<html lang="en">
<head>
<meta charset="utf-8">
<title>VEDRA – Intelligent Data Capture</title>
<link href="https://fonts.googleapis.com/css2?family=Source+Sans+3:wght@400;600;700&family=Oswald:wght@500&family=Arimo:wght@400&display=swap" rel="stylesheet">
<style>
:root{
  --navy:#0d3d66;
  --blue:#1f6fa3;
  --blue-mid:#2d86bd;
  --blue-light:#4ea3cf;
  --sky:#c7ebf7;
  --green:#86bf2c;
  --ink:#333;
  --muted:#555;
  --page:#e9ebec;
  --panel:#f4f4f4;
  --footer:#333;
}
*{margin:0;padding:0;box-sizing:border-box}
html,body{width:947px;height:1200px;overflow:hidden}
body{position:relative;background:var(--page);font-family:"Source Sans 3",sans-serif;color:var(--ink)}
.abs{position:absolute}
.topline{left:0;top:0;width:947px;height:6px;background:var(--navy)}
.header{left:0;top:6px;width:947px;height:98px;background:linear-gradient(#fafafa,#eef0f1)}
.sheet{left:86px;top:104px;width:774px;height:1012px;background:#fff}
.logo{left:88px;top:20px;display:flex;align-items:center;gap:8px}
.logo-dot{width:48px;height:48px;border-radius:50%;background:var(--blue)}
.logo-name{font-size:32px;font-weight:600;color:#7aa9c6;letter-spacing:.5px}
.callus{right:89px;top:33px;font-size:14px;color:#666}
.callus span{color:var(--blue)}
.nav{left:86px;top:76px;width:774px;height:28px;display:flex;gap:2px}
.nav a{flex:auto;display:flex;align-items:center;justify-content:center;font-size:10.5px;font-weight:600;color:#222;text-decoration:none;background:linear-gradient(#fdfdfd,#e4e4e4);border:1px solid #ccc;border-bottom:none;border-radius:3px 3px 0 0}
.nav a.current{background:var(--blue);color:#fff;border-color:var(--blue);flex:0 0 70px}
.news{left:86px;top:104px;width:774px;height:45px;background:linear-gradient(var(--blue),#1b6596);display:flex;align-items:center;color:#fff;border-radius:0 0 3px 3px}
.news-label{width:77px;text-align:center;font-size:14px;border-right:1px solid #8cbbd8;height:28px;line-height:28px}
.news-text{padding:0 12px 0 14px;font-size:7.4px;line-height:14px}
.hero{left:95px;top:158px;width:757px;height:222px;border:1px solid #cbd3da;border-radius:5px;overflow:hidden}
.hero-photo{width:100%;height:100%;background:linear-gradient(100deg,#e8f2fa 0%,#c9dced 45%,#6d8fb0 62%,#24416a 80%,#1b3050 100%)}
.hero-caption{left:0;top:68px;width:318px;height:113px;background:rgba(255,255,255,.45);padding:18px 0 0 29px}
.hero-caption h1{font-family:"Oswald",sans-serif;font-weight:500;font-size:30px;color:#111;line-height:34px}
.hero-caption h2{font-size:16.5px;font-weight:400;color:var(--blue);margin-top:4px}
.hero-caption p{font-size:7.5px;color:var(--blue);margin-top:3px}
.dots{right:11px;bottom:10px;display:flex;gap:2px}
.dots i{width:9px;height:9px;background:var(--blue-light)}
.dots i.on{background:#fff}
.process{left:86px;top:390px}
.welcome-title{left:98px;top:731px;font-size:17px;color:var(--blue)}
.video{left:98px;top:762px;width:221px;height:140px;border:2px solid #222;background:#111}
.video-frame{left:2px;top:2px;width:213px;height:118px;background:linear-gradient(90deg,#2a2a2a,#4a4a4a 40%,#262626)}
.play{left:88px;top:38px;width:44px;height:40px;background:rgba(0,0,0,.55);border-radius:4px}
.controls{left:0;bottom:0;width:217px;height:16px;background:#1a1a1a;display:flex;align-items:center;gap:6px;padding:0 6px;font-size:8px;color:#ccc;font-family:Arimo,sans-serif}
.bar{flex:1;height:4px;background:#444;position:relative}
.bar b{position:absolute;left:0;top:0;width:45%;height:4px;background:#999}
.intro{left:336px;top:757px;width:224px;font-size:7.7px;line-height:14px;color:#444;text-align:justify}
.intro p+p{margin-top:14px}
.contact{left:577px;top:748px;width:277px;height:146px;border-radius:4px;overflow:hidden;background:linear-gradient(135deg,#2179b0,#3a96c9)}
.contact-photo{right:0;top:0;width:118px;height:146px;background:linear-gradient(90deg,rgba(58,150,201,0),#e7cfa8 45%,#d7b48a)}
.contact-body{left:20px;top:14px;color:#fff}
.contact-body h3{font-size:16px;font-weight:400;line-height:19px}
.contact-body h3 span{display:block;color:#9fd3f2}
.contact-body p{font-size:10px;line-height:14px;margin-top:4px}
.contact-body p.gap{margin-top:8px}
.card{top:920px;width:248px;height:149px}
.card-head{height:36px;background:linear-gradient(#2f8ac3,#1a6aa0);display:flex;align-items:center;gap:12px;padding-left:14px;color:#fff;font-size:16.5px}
.card-body{height:82px;background:var(--panel);padding:12px 0 0 16px;font-family:Arimo,sans-serif}
.card-body h4{font-family:"Source Sans 3",sans-serif;font-weight:400;font-size:12.5px;color:var(--blue);position:relative;padding-left:15px}
.card-body h4:before{content:"";position:absolute;left:2px;top:4px;border:3px solid transparent;border-left:4px solid var(--blue)}
.card-body p{font-size:9px;line-height:13px;color:#555;padding-left:15px;margin-top:2px}
.card-body time{display:block;font-size:9px;color:#222;padding-left:15px;margin-top:5px}
.card-foot{margin-top:3px;height:28px;background:var(--panel);text-align:right;padding:8px 20px 0 0;font-size:11.5px;color:var(--blue)}
.footer{left:0;top:1116px;width:947px;height:84px;background:var(--footer);color:#fff}
.footer-nav{left:86px;top:16px;display:flex;font-size:8.5px}
.footer-nav a{color:#fff;text-decoration:none}
.footer-nav span{margin:0 17px;color:#ddd}
.copy{left:86px;top:39px;font-size:9px}
.social{top:24px;width:20px;height:20px;border-radius:50%;background:#555}
</style>
</head>
<body>
<div class="abs topline"></div>
<div class="abs header"></div>
<div class="abs sheet"></div>

<div class="abs logo"><span class="logo-dot"></span><span class="logo-name">VEDRA</span></div>
<div class="abs callus">Call Us : <span>00 0000 000 000</span></div>

<nav class="abs nav">
  <a class="current" href="#">HOME</a><a href="#">ABOUT</a><a href="#">SOLUTIONS</a><a href="#">INTELLIGENT DATA CAPTURE</a><a href="#">PRODUCTS</a><a href="#">CUSTOMERS</a><a href="#">FAQ</a><a href="#">CONTACT US</a>
</nav>

<div class="abs news">
  <div class="news-label">News :</div>
  <div class="news-text">Lorem Ipsum is simply dummy text of the printing and typesetting industry. Lorem Ipsum has been the industry's standard dummy text ever since the 1500s, when an unknown printer took a galley of type and scrambled it to make a type specimen book.</div>
</div>

<section class="abs hero">
  <div class="hero-photo" role="img" aria-label="Office photo of three smiling colleagues giving thumbs up at a laptop"></div>
  <div class="abs hero-caption">
    <h1>VEDRA</h1>
    <h2>Intelligent data capture from online sites</h2>
    <p>Lorem Ipsum is simply dummy text of the printing and typesetting industry.</p>
  </div>
  <div class="abs dots"><i class="on"></i><i></i><i></i><i></i><i></i></div>
</section>

<svg class="abs process" width="774" height="320" viewBox="86 390 774 320" font-family="Source Sans 3, sans-serif">
  <g fill="#4a98c0" stroke="#d5edf6" stroke-width="3">
    <circle cx="350" cy="418" r="23"/><circle cx="483" cy="418" r="23"/><circle cx="616" cy="418" r="23"/><circle cx="762" cy="418" r="23"/>
  </g>
  <g fill="#fff" font-size="17" font-weight="700" text-anchor="middle">
    <text x="350" y="424">01</text><text x="483" y="424">02</text><text x="616" y="424">03</text><text x="762" y="424">04</text>
  </g>
  <g fill="#c7ebf7">
    <circle cx="357" cy="526" r="56"/><circle cx="483" cy="500" r="50"/><circle cx="622" cy="500" r="50"/>
    <circle cx="770" cy="572" r="82"/>
    <circle cx="357" cy="652" r="50"/><circle cx="488" cy="652" r="50"/><circle cx="624" cy="652" r="50"/>
  </g>
  <polygon points="377,554 675,554 685,575 675,596 364,596" fill="#86bf2c"/>
  <polygon points="415,570 423,575 415,580" fill="#fff"/>
  <text x="450" y="581" fill="#fff" font-size="14">TOUCHLESS PROCESSING</text>
  <g fill="#3d8db3" stroke="#e9f6fb" stroke-width="2">
    <circle cx="299" cy="488" r="30"/><circle cx="299" cy="564" r="30"/>
  </g>
  <circle cx="299" cy="476" r="8" fill="#d8262a"/>
  <path d="M295 472l8 8M303 472l-8 8" stroke="#fff" stroke-width="2"/>
  <circle cx="299" cy="559" r="8" fill="#6cb81f"/>
  <path d="M295 559l3 3 5-6" stroke="#fff" stroke-width="2" fill="none"/>
  <g fill="#fff" font-size="7" text-anchor="middle">
    <text x="299" y="495">DO NOT</text><text x="299" y="504">MATCH</text><text x="299" y="578">MATCH</text>
  </g>
  <g><rect x="343" y="500" width="6" height="26" fill="#6cb81f"/><rect x="351" y="508" width="6" height="18" fill="#3f7fc4"/><rect x="359" y="514" width="6" height="12" fill="#e98a1c"/></g>
  <g fill="#2b7fb0" font-size="10" text-anchor="middle">
    <text x="357" y="543">3-WAY</text><text x="357" y="555">MATCHING</text>
    <text x="483" y="513" font-size="8">EXCEPTION</text><text x="483" y="522" font-size="8">HANDLING</text><text x="483" y="531" font-size="8">WORKFLOW</text>
    <text x="622" y="516" font-size="9.5">AUTHORIZATION</text>
    <text x="357" y="667" font-size="8.5">MULTI - LEVEL</text><text x="357" y="678" font-size="8.5">REVIEW</text>
    <text x="488" y="662" font-size="8">GL ACCOUNT</text><text x="488" y="672" font-size="8">COST CENTER</text><text x="488" y="684" font-size="8.5">CONDING</text>
    <text x="624" y="666" font-size="8.5">MULTI - LEVEL</text><text x="624" y="677" font-size="8.5">APPROVAL</text>
    <text x="770" y="547" font-size="18" fill="#3a7fa8">POSTING</text>
  </g>
  <circle cx="474" cy="475" r="6" fill="#d8262a"/><circle cx="492" cy="475" r="6" fill="#6cb81f"/>
  <path d="M476 486l14 12M490 486l-14 12" stroke="#e98a1c" stroke-width="3"/>
  <g fill="#fff" stroke="#7a8a99">
    <rect x="608" y="476" width="14" height="18"/><rect x="336" y="630" width="13" height="16"/><rect x="480" y="622" width="16" height="20"/><rect x="602" y="628" width="13" height="16"/>
  </g>
  <path d="M614 488l4 4 7-8M340 641l3 3 6-7M606 639l3 3 6-7" stroke="#6cb81f" stroke-width="2" fill="none"/>
  <rect x="493" y="626" width="8" height="8" fill="#6cb81f"/>
  <g fill="#e0a46b"><circle cx="359" cy="635" r="4"/><circle cx="369" cy="635" r="4"/><circle cx="632" cy="633" r="4"/><circle cx="642" cy="633" r="4"/></g>
  <g fill="#3f7fc4"><rect x="354" y="640" width="10" height="7" rx="3"/><rect x="364" y="640" width="10" height="7" rx="3"/><rect x="627" y="638" width="10" height="7" rx="3"/><rect x="637" y="638" width="10" height="7" rx="3"/></g>
  <rect x="738" y="566" width="18" height="48" fill="#dcdcdc" stroke="#888"/>
  <rect x="754" y="556" width="52" height="40" fill="#2b6fb8" stroke="#333" stroke-width="3"/>
  <path d="M768 577l8 9 16-20" stroke="#f2a31b" stroke-width="4" fill="none"/>
  <rect x="770" y="598" width="20" height="5" fill="#444"/>
  <g fill="#555" font-size="14">
    <text x="148" y="501">INVOICE</text><text x="148" y="519">WITH PO</text>
    <text x="224" y="643" text-anchor="end">INVOICE WITH</text><text x="224" y="662" text-anchor="end">OUT PO</text>
  </g>
  <polygon points="216,500 238,500 238,494 254,506 238,518 238,512 216,512" fill="#86bf2c"/>
  <polygon points="236,639 258,639 258,633 274,645 258,657 258,651 236,651" fill="#86bf2c"/>
</svg>

<h2 class="abs welcome-title" style="font-weight:400">Welcome to VEDRA</h2>

<div class="abs video">
  <div class="abs video-frame" role="img" aria-label="Video still of two business women in an interview"></div>
  <div class="abs play"><svg width="44" height="40"><polygon points="16,10 32,20 16,30" fill="#2a8fe0"/></svg></div>
  <div class="abs controls"><span>❚❚</span><span>0:04 / 0:30</span><div class="bar"><b></b></div></div>
</div>

<div class="abs intro">
  <p>Lorem Ipsum is simply dummy text of the printing and typesetting industry. Lorem Ipsum has been the industry's standard dummy text ever since the 1500s, when an unknown printer took a galley of type and scrambled.</p>
  <p>It to make a type specimen book. It has survived not only five centuries, but also the leap into electronic typesetting, remaining essentially unchanged. It was popularised in the 1960s with the release of Letraset sheets containing Lorem Ipsum passages, and more recently.</p>
</div>

<aside class="abs contact">
  <div class="abs contact-photo" role="img" aria-label="Photo of a smiling support agent on the phone beside a computer"></div>
  <div class="abs contact-body">
    <h3>Contact <span>VEDRA</span></h3>
    <p>Lorem Ipsum is simply dummy<br>Lorem Ipsum is dummy<br>Lorem Ipsum is the simply.</p>
    <p class="gap">Call Us : 00 0000 000 000<br>Email Us : vedra@info.com</p>
  </div>
</aside>

<section class="abs card" style="left:95px">
  <div class="card-head"><svg width="32" height="28"><path d="M3 12l13 9 13-9v14H3z" fill="#fff"/><circle cx="16" cy="8" r="5" fill="#fff"/></svg>Latest News</div>
  <div class="card-body"><h4>Mauris commodo feugiat</h4><p>Nulla facilisi. Curabitur at elit ligula,<br>eget hendrerit felis vehicula.</p><time>Dec-26-2012</time></div>
  <div class="card-foot">View All ▸</div>
</section>
<section class="abs card" style="left:351px">
  <div class="card-head"><svg width="26" height="26"><rect x="3" y="5" width="20" height="19" fill="none" stroke="#fff" stroke-width="2"/><rect x="3" y="5" width="20" height="5" fill="#fff"/><path d="M8 14h10M8 19h10M10 12v10M16 12v10" stroke="#fff"/></svg>Latest Events</div>
  <div class="card-body"><h4>Mauris commodo feugiat</h4><p>Nulla facilisi. Curabitur at elit ligula,<br>eget hendrerit felis vehicula.</p><time>Dec-26-2012</time></div>
  <div class="card-foot">View All ▸</div>
</section>
<section class="abs card" style="left:606px">
  <div class="card-head"><svg width="34" height="26"><ellipse cx="14" cy="11" rx="12" ry="8" fill="#fff"/><ellipse cx="22" cy="15" rx="10" ry="7" fill="#fff" stroke="#2a7fb6"/><path d="M6 17l-2 6 7-4" fill="#fff"/></svg>Latest Blog</div>
  <div class="card-body"><h4>Mauris commodo feugiat</h4><p>Nulla facilisi. Curabitur at elit ligula,<br>eget hendrerit felis vehicula.</p><time>Dec-26-2012</time></div>
  <div class="card-foot">View All ▸</div>
</section>

<footer class="abs footer">
  <nav class="abs footer-nav">
    <a href="#">Home</a><span>|</span><a href="#">About</a><span>|</span><a href="#">Solutions</a><span>|</span><a href="#">intelligent data capture</a><span>|</span><a href="#">Products</a><span>|</span><a href="#">Customers</a><span>|</span><a href="#">Faq</a><span>|</span><a href="#">Contact Us</a>
  </nav>
  <p class="abs copy">Copyright © 2013 &nbsp;www.vedra.com &nbsp;All rights reserved.</p>
  <span class="abs social" style="left:813px"></span>
  <span class="abs social" style="left:840px"></span>
</footer>
</body>
</html>
```